Residential Real Estate needs a flyer design

I need a flyer that brings all my companies together to target that person who needs to sell, rent, or refinance their home. We specialize in buying, selling, managing, and providing home loans in El Paso, TX. I have uploaded a document that will give you all my thoughts of this flyer. My companies include Brisk Mortgage Lending (Residential Mortgage Lending), Keystone Realty El Paso (Real Estate Brokerage), Tenant Haven Homes El Paso (Property Management Company), DMR Capital, LLC (Real Estate Investment Manager). I believe home owners need more options in the residential real estate market. Most real estate companies can only sell a home - we can sell, rent, manage, buy or refinance a home. We have the ability to put your home on the market for sale and rent at the same time, which gives you two options at once. We also buy homes as investments (DMR Capital, LLC). All homes purchased are cash buys and can close in 10 days. We specialize in the residential real estate market in El Paso, TX (selling & buying), mortgage lending, and the property management business. Our evaluation is completely free of charge. All companies are under the same management and broker. We have a few thing we use in marketing: 1. We will sell your home in 60 days, or we will buy it....Guaranteed in writing. 2. We will sell your home in 60 days, or we will sell it for free....Guaranteed in writing. 3. We will provide you with an offer to buy your home in 24 hours guaranteed. 4. We will rent your home in 60 days, or we will manage it for free for 1 month. HOW ARE WE DIFFERENT? We are able to provide you with every possible option and educate you in each scenario with guarantees.

• *Certain Restrictions Apply – Call For Details.
• This is not intended to be a solicitation if your home is currently listed with a broker.

```html
<!DOCTYPE html>
<html lang="en">
<head>
<meta charset="UTF-8">
<title>Keystone Realty El Paso – Flyer</title>
<link rel="stylesheet" href="https://fonts.googleapis.com/css2?family=Libre+Baskerville:wght@400;700&family=Open+Sans:wght@700&display=swap">
<style>
  :root {
    --backdrop: #9a9a9a;
    --paper: #ffffff;
    --brand-red: #b51e24;
    --headline-red: #c8202a;
    --ink: #111111;
    --body-ink: #222222;
    --yellow: #f2d21b;
    --cyan: #1fb3e8;
    --green: #2ea23a;
    --magenta: #e8207e;
  }
  * { box-sizing: border-box; margin: 0; padding: 0; }
  html, body { width: 1200px; height: 1000px; overflow: hidden; }
  body { background: var(--backdrop); position: relative; font-family: "Libre Baskerville", serif; }

  .flyer {
    position: absolute; left: 320px; top: 28px; width: 708px; height: 916px;
    background: var(--paper); overflow: hidden;
  }
  .hero-photo {
    position: absolute; left: 0; top: 0; width: 708px; height: 366px;
    background: linear-gradient(180deg, #3f6fc4 0%, #7fa6dc 32%, #d8c29a 52%, #c9a97c 66%, #b9b29a 76%, #8a9a52 88%, #6f8a3a 100%);
  }
  .brand-box {
    position: absolute; left: 17px; top: 17px; width: 166px; height: 88px;
    background: var(--paper); display: flex; align-items: center; justify-content: center;
    text-align: center; padding: 8px;
  }
  .brand-name { font-weight: 700; font-size: 16px; line-height: 1.25; color: var(--brand-red); }
  .accent-band { position: absolute; left: 0; top: 366px; width: 708px; height: 16px; background: var(--brand-red); }

  .headline { position: absolute; left: 17px; font-weight: 700; color: var(--ink); font-size: 30px; white-space: nowrap; line-height: 1.2; }
  .headline--one { top: 403px; }
  .headline--two { top: 458px; }
  .headline .expire { color: var(--headline-red); margin-left: 26px; font-size: 31px; }

  .options-title {
    position: absolute; left: 21px; top: 549px; font-weight: 700; font-size: 22px; color: var(--ink); white-space: nowrap;
  }
  .options-dots { position: absolute; left: 424px; top: 539px; display: flex; gap: 11px; }

  .dot { width: 48px; height: 48px; border-radius: 50%; flex: none; }
  .dot--yellow { background: var(--yellow); }
  .dot--cyan { background: var(--cyan); }
  .dot--green { background: var(--green); }
  .dot--magenta { background: var(--magenta); }

  .option { position: absolute; display: flex; align-items: center; gap: 30px;
    font-family: "Open Sans", sans-serif; font-weight: 700; font-size: 18px; color: var(--ink); white-space: nowrap; }
  .option--sell { left: 22px; top: 612px; }
  .option--buy { left: 22px; top: 673px; }
  .option--rent { left: 388px; top: 613px; }
  .option--refi { left: 388px; top: 674px; }

  .about {
    position: absolute; left: 17px; top: 742px; width: 677px; height: 74px; overflow: hidden;
    font-size: 11.6px; line-height: 18.5px; text-align: justify; color: var(--body-ink);
  }

  .cta-band {
    position: absolute; left: 0; top: 842px; width: 708px; height: 74px; background: var(--brand-red);
  }
  .cta-text {
    position: absolute; left: 14px; top: 13px; width: 406px; text-align: center; white-space: nowrap;
    color: #fff; font-weight: 700; font-size: 12.5px; letter-spacing: 0.2px; line-height: 25px;
  }
  .cta-phone { position: absolute; left: 428px; top: 16px; display: flex; align-items: center; gap: 11px; }
  .cta-number { color: #fff; font-weight: 700; font-size: 27px; white-space: nowrap; }
</style>
</head>
<body>
  <main class="flyer">
    <div class="hero-photo" role="img" aria-label="Photo of a single-storey stucco home with a white garage door, driveway and green lawn under a blue sky"></div>
    <div class="brand-box"><span class="brand-name">Keystone Realty El Paso</span></div>
    <div class="accent-band"></div>

    <h1 class="headline headline--one">Give yourself more options.</h1>
    <h2 class="headline headline--two">Don’t let your<span class="expire">HOME EXPIRE AGAIN.</span></h2>

    <p class="options-title">GIVE YOURSELF OPTIONS....</p>
    <div class="options-dots">
      <span class="dot dot--yellow"></span>
      <span class="dot dot--cyan"></span>
      <span class="dot dot--green"></span>
      <span class="dot dot--magenta"></span>
    </div>

    <div class="option option--sell"><span class="dot dot--yellow"></span><span>We can sell your Home</span></div>
    <div class="option option--buy"><span class="dot dot--green"></span><span>Buy your home</span></div>
    <div class="option option--rent"><span class="dot dot--cyan"></span><span>Rent your Home</span></div>
    <div class="option option--refi"><span class="dot dot--magenta"></span><span>Refinance your home</span></div>

    <p class="about">We have the ability to put your home on the market for sale and rent at the same time, which gives you two options at once. All homes purchased are cash buys and can close in 10 days. We specialize in the residential real estate market (selling &amp; buying), mortgage lending, and the property management business. Our evaluation is completely free of charge. All the companies below are under the same management and broker.</p>

    <footer class="cta-band">
      <p class="cta-text">CALL US TODAY TO SCHEDULE AN APPOINTMENT<br>- COMPLETELY FREE OF CHARGE -</p>
      <div class="cta-phone">
        <svg width="38" height="38" viewBox="0 0 38 38"><rect x="0" y="0" width="38" height="38" rx="7" fill="#fff"/><path d="M13 8c-2 1-4 3-3.5 6 1 6 6 13 12 16 3 1 5-1 6-3l-4-4-3 2c-3-2-5-5-6-8l2-3z" fill="var(--brand-red)"/></svg>
        <span class="cta-number">915-555-0148</span>
      </div>
    </footer>
  </main>
</body>
</html>
```